Letterhead needed using basic elements of our new logo!

We have just had a new logo and business card created on Pixel Harbor and now would like a new letterhead for our company re-branding. Our logo inspires trust, professionalism and confidence and we would like to mirror that in our letterhead. We would like to use elements in our logo (as well as the logo itself, obviously), but understand with only a header and the ability to print in black and white, we are somewhat limited. We have also won the Resident's Pick Medal for best Property Management Company in our city and would like to somehow include that small banner (see uploaded file) in the letterhead, without it clashing?

Text to include:
Bright Cove Property Management (and logo)
C-214 Tamblyn Cres, Winnipeg, MB R2K 3P7
Ph: 204-739-8152
Fax: 1-888-376-2914
Email: customerservice@brightcovepropertymanagement.example
Web: www.brightcovepropertymanagement.example

Pasted below is our mission, vision and branding statements to help with the project:

Mission Statement

Provide the highest quality customer service to both property owners and tenants using innovative technology and well trained, caring staff.

Vision Statement

To redefine the way in which management is delivered to its customers, becoming the recognized leader in the property management industry.

Brand Essence

When our customers experience our product or service, it brings forth an emotion of absolute trust that we have their best interests at heart

Brand Personality

We are a company that is passionate about our customers, our company and our vision to be leaders in the field of property management. We are visionaries that aren't afraid to use cutting edge technologies to improve our products and service.

Position or Value Proposition

To whom are we speaking?
- real estate investors, including first timers that are giving us their first starter home. They are fairly naive, as they are not "big time" investors, and because they are giving us their first home (in contract to an investor buying a rental property, often sight unseen) they are more emotionally tied to their property and will require a company that inspires trust and confidence.

What is our brand promise?
- we will do our best to serve our clients, both owners and tenants, to give them prompt communication, clear, concise answers to their questions, and look after their property quickly and competently.

Why is our product different than the competition and why should our customers care?
- the current model used by most management companies employs individual portfolio managers that do things a little differently each instance, and differently than their fellow staff members. Our management product is superior because we use a combination of technology and strict procedures to ensure each client's experience is consistent, each and every time.

Industry/Entity Type

Business

Requirements
Must have
• We would like an option to be in black and white, to be able to be printed from Microsoft Word. As well, we do not want anything in a footer or any other kind of letterhead that bleeds below a header. The main use of this letterhead will be from our property management software, to be used in our form letters and other templates (sent to tenants and clients)
Should not have
• Footer or other elements where the text body would be, it will be used in a form letter

```html
<!DOCTYPE html>
<html lang="en">
<head>
<meta charset="utf-8">
<title>Bright Cove Property Management – Letterhead</title>
<link href="https://fonts.googleapis.com/css2?family=Open+Sans:wght@400;600&display=swap" rel="stylesheet">
<style>
  :root {
    --backdrop: #1f1f29;
    --paper: #ffffff;
    --ink-dark: #3f3f3f;
    --ink-body: #7a7a7a;
    --ink-contact: #8a8a8a;
    --brand: #555555;
  }
  * { margin: 0; padding: 0; box-sizing: border-box; }
  html, body {
    width: 1000px; height: 1200px; overflow: hidden;
    background: var(--backdrop);
    font-family: "Open Sans", Arial, sans-serif;
  }
  .letter {
    position: absolute; left: 164px; top: 117px;
    width: 694px; height: 977px;
    background: var(--paper);
  }
  .brand {
    position: absolute; left: 82px; top: 120px;
    display: flex; align-items: center; gap: 10px;
  }
  .brand-mark { width: 30px; height: 30px; background: var(--brand); }
  .brand-name {
    font-size: 15px; font-weight: 600; color: var(--brand);
    line-height: 18px; letter-spacing: 0.5px; text-transform: uppercase;
  }
  .contact {
    position: absolute; left: 417px; top: 115px;
    font-size: 6.6px; line-height: 13px; color: var(--ink-contact);
    letter-spacing: 0.3px;
  }
  .contact .phone-fax { display: flex; gap: 22px; }
  .contact .web { letter-spacing: 1.1px; }
  .salutation {
    position: absolute; left: 83px; top: 249px;
    font-size: 14px; color: var(--ink-body);
  }
  .body-copy {
    position: absolute; left: 83px; top: 285px; width: 528px;
    font-size: 11.1px; line-height: 15.3px; color: var(--ink-body);
  }
  .body-copy p + p { margin-top: 16px; }
  .body-copy .lead { text-indent: 125px; }
  .signatory {
    position: absolute; left: 81px; top: 786px;
    font-size: 23px; color: var(--ink-dark);
  }
  .closing {
    position: absolute; left: 81px; top: 828px;
    font-size: 8.5px; line-height: 12px; color: var(--ink-dark);
  }
  .date {
    position: absolute; right: 86px; top: 840px;
    font-size: 8.5px; color: var(--ink-dark);
  }
</style>
</head>
<body>
<main class="letter">
  <header>
    <div class="brand">
      <span class="brand-mark"></span>
      <span class="brand-name">Bright Cove<br>Property Management</span>
    </div>
    <address class="contact">
      <div>C-214 Tamblyn Cres, Winnipeg, MB R2K 3P7</div>
      <div class="phone-fax"><span>Phone : 204-739-8152</span><span>Fax: 1-888-376-2914</span></div>
      <div>customerservice@brightcovepropertymanagement.example</div>
      <div class="web">www.brightcovepropertymanagement.example</div>
    </address>
  </header>

  <p class="salutation">Lorem ipsum dolor sit amet,</p>

  <section class="body-copy">
    <p class="lead">Sed ut perspiciatis unde omnis iste natus error sit voluptatem accusantium doloremque laudantium, totam rem aperiam, eaque ipsa quae ab illo inventore veritatis et quasi architecto beatae vitae dicta sunt explicabo. Nemo enim ipsam voluptatem quia voluptas sit aspernatur aut odit aut fugit, sed quia consequuntur magni dolores eos qui ratione voluptatem sequi nesciunt. Neque porro quisquam est, qui dolorem ipsum quia dolor sit amet, consectetur, adipisci velit, sed quia non numquam eius modi tempora incidunt ut labore et dolore magnam aliquam quaerat voluptatem. Ut enim ad minima veniam, quis nostrum exercitationem ullam corporis suscipit laboriosam, nisi ut aliquid ex ea commodi consequatur? Quis autem vel eum iure reprehenderit qui in ea voluptate velit esse quam nihil molestiae consequatur, vel illum qui dolorem eum fugiat quo voluptas nulla pariatur.</p>
    <p>Sed ut perspiciatis unde omnis iste natus error sit voluptatem accusantium doloremque laudantium, totam rem aperiam, eaque ipsa quae ab illo inventore veritatis et quasi architecto beatae vitae dicta sunt explicabo. Nemo enim ipsam voluptatem quia voluptas sit aspernatur aut odit aut fugit, sed quia consequuntur magni dolores eos qui ratione voluptatem sequi nesciunt. Neque porro quisquam est, qui dolorem ipsum quia dolor sit amet, consectetur, adipisci velit, sed quia non numquam eius modi tempora incidunt ut labore et dolore magnam aliquam quaerat voluptatem. Ut enim ad minima veniam, quis nostrum exercitationem ullam corporis suscipit laboriosam, nisi ut aliquid ex ea commodi consequatur? Quis autem vel eum iure reprehenderit qui in ea voluptate velit esse quam nihil molestiae consequatur, vel illum qui dolorem eum fugiat quo voluptas nulla pariatur. Sed ut perspiciatis unde omnis iste natus error sit voluptatem accusantium doloremque laudantium, totam rem aperiam, eaque ipsa quae ab illo inventore veritatis et quasi architecto beatae vitae dicta sunt explicabo. Nemo enim ipsam voluptatem quia voluptas sit aspernatur aut odit aut fugit, sed quia consequuntur magni dolores eos qui ratione voluptatem sequi nesciunt. Neque porro quisquam est, qui dolorem ipsum quia dolor sit amet, consectetur, adipisci velit, sed quia non numquam eius modi tempora incidunt ut labore et dolore magnam aliquam quaerat voluptatem. Ut enim ad minima veniam, quis nostrum exercitationem ullam corporis suscipit laboriosam, nisi ut aliquid ex ea commodi consequatur? Quis autem vel eum iure reprehenderit qui in ea voluptate velit esse quam nihil molestiae consequatur, vel illum qui dolorem eum fugiat quo voluptas nulla pariatur.</p>
  </section>

  <p class="signatory">John Doe</p>
  <p class="closing">Sincerely,<br>Managing Director</p>
  <p class="date">Date: 01 Jan, 2016</p>
</main>
</body>
</html>
```